Design a Flyer For Stainless Steel Chrome Auto Accessories

I have a full product line of chrome accessories (pillar post and rocker panel) selling online and I need couple flyers to show some of the main features of my products and the difference between mine and my competitors.

My requirements for this project are:
the design need to have chrome stainless steel look and feel.
the final design in psd format and 1200px in width and 1800px in height for each page should be OK.
it can be two sections or two separate pages flyer.
first page emphasis the key points I provide in attachment.
second page for products comparison, also provide in attachment.
the layout of first and second page better be different.

Some sample pictures are shared in my dropbox shared folder, please remove background when use in the design.
https://www.filemuleo.net/sh/k4rmqwtzevnpda/QXR7pLmYvTnw83sKw-hd41zxe?dl=0

```html
<!DOCTYPE html>
<html lang="en">
<head>
<meta charset="utf-8">
<title>Stainless Steel Accessories Flyer</title>
<link href="https://fonts.googleapis.com/css2?family=Oswald:wght@500;700&family=Roboto+Condensed:ital,wght@0,400;0,700;1,400&display=swap" rel="stylesheet">
<style>
  :root {
    --backdrop: #d9d9d9;
    --steel-light: #e4e6e8;
    --steel-mid: #a9adb1;
    --steel-dark: #6f7378;
    --graphite: #4a4d51;
    --label-bg: #2f3134;
    --ink: #111214;
    --white: #ffffff;
    --tick: #1f8fe0;
  }
  * { box-sizing: border-box; margin: 0; padding: 0; }
  html, body { width: 1200px; height: 800px; overflow: hidden; }
  body { background: var(--backdrop); position: relative; font-family: "Roboto Condensed", Arial, sans-serif; }

  .page {
    position: absolute; top: 35px; width: 488px; height: 732px; overflow: hidden;
    box-shadow: 0 4px 14px rgba(0,0,0,.35);
  }
  .page--advantages { left: 93px; background: linear-gradient(180deg, var(--steel-mid) 0%, var(--steel-light) 22%, var(--steel-mid) 45%, var(--graphite) 62%, var(--steel-dark) 100%); }
  .page--comparison { left: 608px; width: 491px; background: linear-gradient(90deg, var(--steel-dark) 0%, var(--steel-light) 50%, var(--steel-dark) 100%); }

  .swoosh { position: absolute; left: 0; top: 0; width: 100%; height: 100%; pointer-events: none; }

  .badge { position: absolute; left: 19px; top: 16px; width: 96px; height: 96px; border-radius: 50%;
    background: radial-gradient(circle, #c9ccd0 55%, #7d8186 56%, #e7e9eb 70%, #8a8e93 100%); box-shadow: 0 2px 4px rgba(0,0,0,.4); }

  .headline { position: absolute; left: 130px; top: 44px; font-family: "Oswald", Impact, sans-serif; color: var(--white); text-shadow: 0 2px 3px rgba(0,0,0,.55); line-height: 1; }
  .headline__small { display: block; font-size: 23px; font-weight: 500; letter-spacing: .5px; margin-left: 32px; }
  .headline__big { display: block; font-size: 46px; font-weight: 700; margin-top: 6px; color: #eef0f2; }

  .photo { position: absolute; border-radius: 8px; }
  .photo--hero { left: -6px; top: 118px; width: 190px; height: 160px; background: linear-gradient(135deg, #f4f4f2, #d5d5d0); transform: rotate(-10deg); border-radius: 4px; box-shadow: 0 3px 8px rgba(0,0,0,.4); }
  .photo--thumb { top: 151px; width: 112px; height: 106px; border: 3px solid var(--white); box-shadow: 0 2px 6px rgba(0,0,0,.4); }
  .photo--thumb-a { left: 229px; background: linear-gradient(135deg, #1c1c1c 0%, #8d9096 55%, #e9eaec 100%); }
  .photo--thumb-b { left: 356px; background: linear-gradient(135deg, #2a2a2a 0%, #c9b99a 45%, #efe9dd 100%); }

  .tagline { position: absolute; left: 0; width: 100%; top: 306px; text-align: center; font-weight: 700; font-size: 17px; color: #eeeff0; text-shadow: 0 1px 3px rgba(0,0,0,.7); }

  .label { position: absolute; background: var(--label-bg); color: var(--white); font-family: "Oswald", Impact, sans-serif; font-weight: 700; text-align: center; border: 2px solid #8c9095; border-radius: 5px; box-shadow: 0 2px 5px rgba(0,0,0,.5); }
  .label--advantages { left: 13px; top: 358px; width: 227px; height: 47px; font-size: 24px; line-height: 43px; }
  .label--comparison { left: 128px; top: 8px; width: 243px; height: 47px; font-size: 22px; line-height: 43px; }

  .advantages { position: absolute; left: 22px; top: 426px; width: 440px; list-style: none; color: var(--white); }
  .advantage { margin-bottom: 8px; }
  .advantage__title { font-weight: 700; font-size: 19px; text-shadow: 0 1px 2px rgba(0,0,0,.6); }
  .advantage__text { font-style: italic; font-size: 13.5px; line-height: 1.2; color: #f2f2f2; margin-top: 2px; }

  .column-head { position: absolute; top: 84px; width: 170px; text-align: center; font-family: "Oswald", Impact, sans-serif; font-weight: 700; font-size: 20px; color: var(--ink); }
  .column-head--ours { left: 38px; }
  .column-head--theirs { left: 285px; }

  .caption { position: absolute; width: 190px; text-align: center; font-weight: 700; font-size: 12.5px; color: var(--ink); }
  .caption--ours { left: 28px; }
  .caption--theirs { left: 275px; }

  .shot { position: absolute; width: 117px; height: 111px; border-radius: 9px; border: 3px solid var(--white); box-shadow: 0 2px 5px rgba(0,0,0,.35); }
  .shot--ours { left: 64px; }
  .shot--theirs { left: 311px; }

  .tick { position: absolute; width: 38px; height: 38px; }
  .vs { position: absolute; left: 222px; width: 52px; text-align: center; font-family: "Oswald", Impact, sans-serif; font-weight: 700; font-size: 30px; color: var(--ink); }
</style>
</head>
<body>

<section class="page page--advantages">
  <svg class="swoosh" viewBox="0 0 488 732" aria-hidden="true">
    <path d="M120 28 Q300 0 488 8 L488 0 L100 0 Z" fill="#f7f8f9" opacity=".8"/>
    <path d="M0 352 Q180 345 488 300 L488 350 Q220 380 0 390 Z" fill="#5b5e62" opacity=".75"/>
    <path d="M230 732 Q380 700 488 600 L488 732 Z" fill="#3a3c3f" opacity=".7"/>
    <path d="M200 732 Q360 710 488 620" fill="none" stroke="#f1f2f3" stroke-width="4"/>
  </svg>

  <div class="badge" role="img" aria-label="Round origin badge"></div>

  <h1 class="headline">
    <span class="headline__small">PREMIUM QUALITY</span>
    <span class="headline__big">STAINLESS STEEL</span>
  </h1>

  <div class="photo photo--hero" role="img" aria-label="Polished stainless steel panel"></div>
  <div class="photo photo--thumb photo--thumb-a" role="img" aria-label="Steel panel with protective film peeled back"></div>
  <div class="photo photo--thumb photo--thumb-b" role="img" aria-label="Mirror finish steel panel"></div>

  <p class="tagline">Mirror Polished Finish Products Absolutely Rust-Free</p>

  <h2 class="label label--advantages">OUR ADVANTAGES</h2>

  <ul class="advantages">
    <li class="advantage">
      <h3 class="advantage__title">Fully covered with Tenaxo™ Acrylic Foam Tape</h3>
      <p class="advantage__text">High performance acrylic adhesives</p>
    </li>
    <li class="advantage">
      <h3 class="advantage__title">Beveled Cutting Edge</h3>
      <p class="advantage__text">Creates a classically elegant design that looks amazing compared to cheap sharp cutting.</p>
    </li>
    <li class="advantage">
      <h3 class="advantage__title">Protective Film</h3>
      <p class="advantage__text">Keeps stainless steel spotless to eliminate scrapes or scratches to the stainless steel surface during the transition.</p>
    </li>
    <li class="advantage">
      <h3 class="advantage__title">Heavy-Duty Packaging</h3>
      <p class="advantage__text">Well protected package to prevent scratch and damage.</p>
    </li>
  </ul>
</section>

<section class="page page--comparison">
  <svg class="swoosh" viewBox="0 0 491 732" aria-hidden="true">
    <path d="M0 60 Q60 20 180 0 L0 0 Z" fill="#f4f5f6" opacity=".85"/>
    <path d="M0 68 Q70 28 190 4" fill="none" stroke="#ffffff" stroke-width="3"/>
    <path d="M180 732 Q360 720 491 640 L491 732 Z" fill="#55585c" opacity=".6"/>
    <path d="M150 732 Q350 712 491 650" fill="none" stroke="#f1f2f3" stroke-width="4"/>
  </svg>

  <h2 class="label label--comparison">PRODUCT COMPARISON</h2>

  <h3 class="column-head column-head--ours">OUR PRODUCT</h3>
  <h3 class="column-head column-head--theirs">COMPETITOR</h3>

  <!-- row 1 -->
  <p class="caption caption--ours" style="top:117px">High quality 304 stainless steel</p>
  <p class="caption caption--theirs" style="top:117px">Cheap stainless steel material</p>
  <div class="shot shot--ours" style="top:138px;background:linear-gradient(135deg,#2b2b2b,#b7babe 55%,#f0f1f2)" role="img" aria-label="High quality steel panel"></div>
  <div class="shot shot--theirs" style="top:138px;background:linear-gradient(135deg,#8f9296,#d9dbdd 60%,#f5f5f5)" role="img" aria-label="Cheap steel panel"></div>
  <span class="vs" style="top:176px">VS</span>

  <!-- row 2 -->
  <p class="caption caption--ours" style="top:268px">Fully covered Tenaxo</p>
  <p class="caption caption--theirs" style="top:268px">Partial covered fake Tenaxo tape</p>
  <div class="shot shot--ours" style="top:289px;background:linear-gradient(135deg,#e8e8e8,#d62a33 30%,#b81f28 100%)" role="img" aria-label="Panel back fully covered with red tape"></div>
  <div class="shot shot--theirs" style="top:289px;background:linear-gradient(90deg,#e5ddd2,#c7a98a 30%,#e9e4dc 50%,#c7a98a 70%,#e5ddd2)" role="img" aria-label="Panel back with partial tape strips"></div>
  <span class="vs" style="top:327px">VS</span>

  <!-- row 3 -->
  <p class="caption caption--ours" style="top:418px">Beveled Cutting Edge</p>
  <p class="caption caption--theirs" style="top:418px">Cheap look cutting edge</p>
  <div class="shot shot--ours" style="top:439px;background:linear-gradient(135deg,#1a1a1a,#6d7075 50%,#d8dadc)" role="img" aria-label="Beveled panel edge"></div>
  <div class="shot shot--theirs" style="top:439px;background:linear-gradient(135deg,#f3f1ea,#c8bea8 55%,#efeae0)" role="img" aria-label="Sharp cut panel edge"></div>
  <span class="vs" style="top:477px">VS</span>

  <!-- row 4 -->
  <p class="caption caption--ours" style="top:559px">Protective Film</p>
  <p class="caption caption--theirs" style="top:559px">Plastic Film</p>
  <div class="shot shot--ours" style="top:580px;background:linear-gradient(135deg,#dfe4ea,#1b1b1b 55%,#7c8086)" role="img" aria-label="Panel with protective film"></div>
  <div class="shot shot--theirs" style="top:580px;background:linear-gradient(135deg,#5a5d62,#d4cfc4 45%,#f2f0ea)" role="img" aria-label="Panel with plastic film"></div>
  <span class="vs" style="top:618px">VS</span>

  <!-- ticks -->
  <svg class="tick" style="left:62px;top:212px" viewBox="0 0 38 38" aria-hidden="true"><rect x="2" y="8" width="26" height="26" fill="#fff" stroke="var(--tick)" stroke-width="3"/><path d="M8 20 L15 28 L35 4" fill="none" stroke="var(--tick)" stroke-width="5"/></svg>
  <svg class="tick" style="left:62px;top:363px" viewBox="0 0 38 38" aria-hidden="true"><rect x="2" y="8" width="26" height="26" fill="#fff" stroke="var(--tick)" stroke-width="3"/><path d="M8 20 L15 28 L35 4" fill="none" stroke="var(--tick)" stroke-width="5"/></svg>
  <svg class="tick" style="left:62px;top:513px" viewBox="0 0 38 38" aria-hidden="true"><rect x="2" y="8" width="26" height="26" fill="#fff" stroke="var(--tick)" stroke-width="3"/><path d="M8 20 L15 28 L35 4" fill="none" stroke="var(--tick)" stroke-width="5"/></svg>
  <svg class="tick" style="left:62px;top:654px" viewBox="0 0 38 38" aria-hidden="true"><rect x="2" y="8" width="26" height="26" fill="#fff" stroke="var(--tick)" stroke-width="3"/><path d="M8 20 L15 28 L35 4" fill="none" stroke="var(--tick)" stroke-width="5"/></svg>
</section>

</body>
</html>
```